Restumping company needs business cards

We need a business card that reflects all the information in the attached file.

Back side to just have the logo (see attached image as an example)

All information to be on the front side

Front side must contain;
Logo
Dale Morrow (Director)
Ph: 1800 472 915
Mob: 0412 687 143
Email: dale@keystonebase.com.au
website: keystonebase.com.au
Call us for a free quote today

Must also contain the words RESTUMPING - SUB FLOOR REPAIRS - RELEVELING

we would like colour scheme to be as per the attached file but open to new suggestions.

Requirements
Must have
• Certified Site Constructor logo
• Crafted Trades Guild Logo
• small snapgrid & pagebook symbol

```html
<!DOCTYPE html>
<html lang="en">
<head>
<meta charset="utf-8">
<title>Keystone Base – Business Card</title>
<link href="https://fonts.googleapis.com/css2?family=Roboto:wght@400;500;700&display=swap" rel="stylesheet">
<style>
  :root {
    --navy: #1e205f;
    --grey: #555a60;
    --muted: #8a8d92;
    --white: #ffffff;
    --page: #ecebe8;
    --rule: #c9cad3;
  }
  * { box-sizing: border-box; margin: 0; padding: 0; }
  html, body { width: 1125px; height: 1200px; overflow: hidden; }
  body {
    background: var(--page);
    font-family: "Roboto", Arial, sans-serif;
    position: relative;
  }
  .card {
    position: absolute;
    left: 166px;
    width: 800px;
    height: 457px;
    box-shadow: 0 3px 8px rgba(0,0,0,0.25);
    overflow: hidden;
  }
  /* Front */
  .card--front { top: 103px; background: var(--white); }
  .brand {
    position: absolute;
    left: 80px; top: 209px;
    display: flex; align-items: center; gap: 10px;
  }
  .brand__mark { width: 20px; height: 20px; background: var(--navy); flex: none; }
  .brand__name {
    font-weight: 700; font-size: 26px; color: var(--navy); letter-spacing: 0.3px;
    white-space: nowrap;
  }
  .divider {
    position: absolute; left: 375px; top: 155px;
    width: 1px; height: 147px; background: var(--rule);
  }
  .person { position: absolute; left: 405px; top: 155px; }
  .person__name { font-size: 29px; font-weight: 700; color: var(--navy); line-height: 1.1; }
  .person__role { font-size: 20px; font-weight: 500; color: var(--muted); margin-top: 2px; }
  .contacts { list-style: none; margin-top: 12px; }
  .contacts li {
    display: flex; align-items: center; gap: 10px;
    font-size: 19.5px; color: var(--grey); height: 24px;
  }
  .contacts svg { width: 15px; height: 15px; fill: var(--navy); flex: none; }
  .web-band {
    position: absolute; left: 0; bottom: 0; width: 100%; height: 40px;
    background: var(--navy); color: var(--white);
    display: flex; align-items: center; justify-content: center;
    font-size: 19px; letter-spacing: 3.4px;
  }
  /* Back */
  .card--back { top: 619px; background: var(--navy); color: var(--white); }
  .social {
    position: absolute; right: 36px; top: 44px;
    display: flex; gap: 10px; font-size: 13px; font-weight: 500;
  }
  .social span { display: flex; align-items: center; gap: 5px; }
  .social span::before {
    content: ""; width: 12px; height: 12px; border-radius: 50%; background: var(--white);
  }
  .wordmark {
    position: absolute; left: 0; top: 150px; width: 100%;
    display: flex; align-items: center; justify-content: center; gap: 16px;
  }
  .wordmark__mark { width: 36px; height: 36px; background: var(--white); flex: none; }
  .wordmark__name { font-size: 50px; font-weight: 700; line-height: 1; letter-spacing: 0.5px; }
  .badges {
    position: absolute; left: 125px; top: 312px; width: 550px;
    display: flex; justify-content: space-between; align-items: center;
  }
  .badge { background: var(--white); opacity: 0.92; }
  .badge--cert { width: 40px; height: 40px; border-radius: 50%; }
  .badge--alliance { width: 160px; height: 34px; border-radius: 4px; }
  .badge--guild { width: 110px; height: 56px; }
  .services-rule {
    position: absolute; left: 137px; top: 381px; width: 529px; height: 1px;
    background: var(--rule);
  }
  .services {
    position: absolute; left: 0; top: 396px; width: 100%;
    display: flex; justify-content: center; align-items: center; gap: 18px;
    font-size: 18px; letter-spacing: 0.4px;
  }
  .services .dot { width: 6px; height: 6px; border-radius: 50%; background: var(--white); }
</style>
</head>
<body>
  <section class="card card--front">
    <div class="brand">
      <span class="brand__mark"></span>
      <span class="brand__name">KEYSTONE BASE</span>
    </div>
    <div class="divider"></div>
    <div class="person">
      <h1 class="person__name">Dale Morrow</h1>
      <p class="person__role">Director</p>
      <ul class="contacts">
        <li><svg viewBox="0 0 16 16"><path d="M3.5 1l3 3-1.6 2a9 9 0 0 0 5 5l2-1.6 3 3-2 2C6 14 2 10 1.5 3z"/></svg>1800 472 915</li>
        <li><svg viewBox="0 0 16 16"><path d="M4 0h8a1 1 0 0 1 1 1v14a1 1 0 0 1-1 1H4a1 1 0 0 1-1-1V1a1 1 0 0 1 1-1zm1 2v10h6V2zm3 11a1 1 0 1 0 0 2 1 1 0 0 0 0-2z"/></svg>0412 687 143</li>
        <li><svg viewBox="0 0 16 16"><path d="M1 4h14v9H1zm1 1l6 4 6-4"/></svg>dale@keystonebase.com.au</li>
      </ul>
    </div>
    <div class="web-band">www.keystonebase.com.au</div>
  </section>

  <section class="card card--back">
    <div class="social"><span>snapgrid</span><span>pagebook</span></div>
    <div class="wordmark">
      <span class="wordmark__mark"></span>
      <span class="wordmark__name">KEYSTONE BASE</span>
    </div>
    <div class="badges">
      <div class="badge badge--cert" role="img" aria-label="Certified Site Constructor badge"></div>
      <div class="badge badge--alliance" role="img" aria-label="Home Trade Alliance member badge"></div>
      <div class="badge badge--guild" role="img" aria-label="Crafted Trades Guild badge"></div>
    </div>
    <div class="services-rule"></div>
    <div class="services">
      <span>RESTUMPING</span><span class="dot"></span>
      <span>SUB FLOOR REPAIRS</span><span class="dot"></span>
      <span>RELEVELING</span>
    </div>
  </section>
</body>
</html>
```